Brett Olsen Building Business Card Design

Hi,

I need a business card for my Building company.
I am a Builder and build homes for clients.
I am looking for a sophisticated logo that can be used on business cards, envelopes and letter heads.
I am trying to take my business to the next level and need a professional business card.

Colours: Please use white, black, dark grey and bright blue.

Thank you,

Carol and Brett.

Target Market(s)

1. Home and Building Companies 2. Potential customers

Industry/Entity Type

Business

Contact Information for Business Card

Brett Olsen Building PTY LTD

Brett Olsen

Director

A.B.N. 37 829 516 073

BUILDERS LICENCE No. 573019k

Mobile: 0412 907 381

Email: brettolsenbuilding@mailvane.com.au

Requirements
Must have
• The following is compulsory to have in the designs:

Brett Olsen Building PTY LTD (business name)

Brett Olsen (contact name)

Director (position)

A.B.N. 37 829 516 073

Builders Licence No. 573019k

Mobile: 0412 907 381

Nice to have
• Logo for business
Should not have
• Should not be cluttered.

I am looking for a clean, sophisticated and professional business card design.

```html
<!DOCTYPE html>
<html lang="en">
<head>
<meta charset="utf-8">
<title>Brett Olsen Building – Business Card</title>
<link href="https://fonts.googleapis.com/css2?family=Lato:wght@300;400;700&display=swap" rel="stylesheet">
<style>
  :root {
    --page-bg: #eceae6;
    --card-front: #023c59;
    --card-band: #012b42;
    --card-back: #00283d;
    --back-mark: #0d4462;
    --ink-white: #ffffff;
    --ink-soft: #e3edf3;
    --card-shadow: 0 6px 14px rgba(0, 0, 0, 0.35);
  }
  * { box-sizing: border-box; margin: 0; padding: 0; }
  html, body {
    width: 1200px;
    height: 1000px;
    overflow: hidden;
    background: var(--page-bg);
    font-family: "Lato", sans-serif;
  }
  .sheet {
    position: relative;
    width: 1200px;
    height: 1000px;
  }
  .card {
    position: absolute;
    top: 349px;
    width: 538px;
    height: 302px;
    box-shadow: var(--card-shadow);
    overflow: hidden;
  }
  .card--front { left: 46px; background: var(--card-front); }
  .card--back { left: 617px; background: var(--card-back); }

  .holder {
    position: absolute;
    left: 40px;
    top: 52px;
    color: var(--ink-white);
  }
  .holder__name {
    font-weight: 700;
    font-size: 24px;
    line-height: 28px;
  }
  .holder__role {
    font-weight: 400;
    font-size: 24px;
    line-height: 26px;
    padding-left: 26px;
  }

  .company {
    position: absolute;
    right: 40px;
    top: 54px;
    display: flex;
    align-items: center;
    gap: 10px;
  }
  .company__square {
    width: 38px;
    height: 38px;
    background: var(--ink-white);
  }
  .company__name {
    color: var(--ink-white);
    font-weight: 400;
    font-size: 15px;
    line-height: 19px;
  }

  .details-band {
    position: absolute;
    left: 0;
    top: 200px;
    width: 100%;
    height: 72px;
    background: var(--card-band);
    display: flex;
    justify-content: space-between;
    padding: 12px 14px 0 12px;
    color: var(--ink-soft);
    font-size: 15px;
  }
  .contact-list, .reg-list { list-style: none; }
  .contact-list li {
    display: flex;
    align-items: center;
    gap: 8px;
    height: 26px;
  }
  .reg-list li {
    text-align: right;
    height: 26px;
    line-height: 26px;
  }
  .icon { width: 20px; height: 20px; flex: none; }

  .back-mark {
    position: absolute;
    inset: 0;
    display: flex;
    align-items: center;
    justify-content: center;
    gap: 14px;
    color: var(--back-mark);
    font-weight: 700;
    font-size: 30px;
  }
  .back-mark__square {
    width: 46px;
    height: 46px;
    background: var(--back-mark);
  }
</style>
</head>
<body>
<main class="sheet">
  <section class="card card--front" aria-label="Business card front">
    <div class="holder">
      <p class="holder__name">Brett Olsen</p>
      <p class="holder__role">director</p>
    </div>

    <div class="company">
      <span class="company__square"></span>
      <p class="company__name">Brett Olsen<br>Building PTY LTD</p>
    </div>

    <div class="details-band">
      <ul class="contact-list">
        <li>
          <svg class="icon" viewBox="0 0 20 20" aria-hidden="true">
            <circle cx="10" cy="10" r="9" fill="none" stroke="#fff" stroke-width="1.4"/>
            <rect x="7" y="4.5" width="6" height="11" rx="1" fill="none" stroke="#fff" stroke-width="1.3"/>
            <rect x="8.2" y="6" width="3.6" height="4" fill="#fff"/>
          </svg>
          <span>0412 907 381</span>
        </li>
        <li>
          <svg class="icon" viewBox="0 0 20 20" aria-hidden="true">
            <circle cx="10" cy="10" r="9.5" fill="#fff"/>
            <rect x="5" y="6.5" width="10" height="7" fill="none" stroke="#012b42" stroke-width="1.3"/>
            <path d="M5 6.5 L10 10.8 L15 6.5" fill="none" stroke="#012b42" stroke-width="1.3"/>
          </svg>
          <span>brettolsenbuilding@mailvane.com.au</span>
        </li>
      </ul>
      <ul class="reg-list">
        <li>A.B.N. 37 829 516 073</li>
        <li>BUILDERS LICENCE No. 573019k</li>
      </ul>
    </div>
  </section>

  <section class="card card--back" aria-label="Business card back">
    <div class="back-mark">
      <span class="back-mark__square"></span>
      <span>Brett Olsen Building</span>
    </div>
  </section>
</main>
</body>
</html>
```